Need a website for our company

We need a website for our company to showcase all our work for customers to see.
We do all phases of home improvement:
Dormers/Extensions
Basement Remodel
Masonry/Concrete/Pavers/Asphalt
Cultured Stone Veneer
Kitchens
Bathrooms
Pool designs
Outdoor Bathroom
Outdoor Kitchens
Tile work
For reference, something similar to this website: https://brightlanebuilders.example/
Target Market(s)
We are trying to target homeowners.
Coding
Coded - Design and coding required
Number of Pages Required
5+ page
Look and feel

```html
<!DOCTYPE html>
<html lang="en">
<head>
<meta charset="utf-8">
<title>Harlow &amp; Sons Construction Inc</title>
<link href="https://fonts.googleapis.com/css2?family=Poppins:wght@400;500;600;700;800&display=swap" rel="stylesheet">
<style>
:root{
  --ink:#111111;
  --white:#ffffff;
  --band:#5b5b5b;
  --band-dark:#4e4e4e;
  --footer-bg:#fbf4f3;
  --muted:#555555;
  --hero-a:#b9b4ad;
  --hero-b:#7d7a75;
}
*{box-sizing:border-box;margin:0;padding:0}
html,body{width:1200px;height:3573px;overflow:hidden}
body{position:relative;font-family:'Poppins',sans-serif;color:var(--ink);background:var(--white)}
.abs{position:absolute}
.btn{position:absolute;display:flex;align-items:center;justify-content:center;border-radius:31px;font-size:17px;font-weight:500;text-transform:uppercase}
.btn-dark{background:var(--ink);color:var(--white)}
.btn-light{background:var(--white);color:var(--ink)}

/* header */
.site-header{position:absolute;left:0;top:0;width:1200px;height:93px;background:var(--white)}
.brand{position:absolute;left:186px;top:26px;display:flex;align-items:center;gap:8px;font-size:17px;font-weight:700;color:var(--ink)}
.brand-mark{width:14px;height:14px;background:var(--ink)}
.main-nav{position:absolute;left:400px;top:31px;font-size:17px}
.main-nav span{position:absolute;white-space:nowrap}
.query-pill{position:absolute;left:951px;top:4px;width:173px;height:71px;border-radius:36px;background:#444;color:var(--white);text-align:center;font-size:17px;line-height:26px;padding-top:10px}

/* hero */
.hero{position:absolute;left:0;top:93px;width:1200px;height:550px;background:linear-gradient(120deg,var(--hero-a),var(--hero-b))}
.hero-tag{position:absolute;left:110px;top:93px;width:280px;height:52px;background:var(--white);display:flex;align-items:center;justify-content:center;font-size:13px;font-weight:600;color:var(--muted);letter-spacing:.6px}
.hero-title{position:absolute;left:110px;top:200px;font-size:58px;font-weight:800;line-height:53px;color:var(--white);text-transform:uppercase}
.hero-copy{position:absolute;left:116px;top:380px;width:445px;font-size:14.5px;line-height:21px;color:var(--white);text-transform:uppercase}

/* about */
.section-title{position:absolute;font-size:36px;font-weight:600;text-transform:uppercase}
.about-rule{position:absolute;left:110px;top:817px;width:155px;height:2px;background:var(--ink)}
.about-copy{position:absolute;left:110px;top:830px;width:430px;font-size:16px;line-height:20.6px}
.photo{position:absolute}

/* services */
.services{position:absolute;left:0;top:1305px;width:1200px;height:917px;background:linear-gradient(180deg,var(--band),var(--band-dark))}
.center-title{position:absolute;left:0;width:1200px;text-align:center;font-size:36px;font-weight:600;color:var(--white);text-transform:uppercase}
.title-rule{position:absolute;left:554px;top:1441px;width:86px;height:2px;background:var(--white)}
.service-card{position:absolute;top:1524px;width:450px;height:586px;background:var(--white)}
.service-card .pic{position:absolute;left:13px;top:17px;width:424px;height:293px}
.service-card h3{position:absolute;left:0;top:336px;width:450px;text-align:center;font-size:27px;font-weight:500}
.service-card p{position:absolute;left:5px;top:391px;width:440px;text-align:center;font-size:15.5px;line-height:20.6px}
.arrow{position:absolute;top:1778px}

/* contact */
.field{position:absolute;left:597px;width:464px;height:41px;border:1px solid #888;font-size:13px;color:#666;padding:11px 11px;text-transform:uppercase}

/* blogs */
.blogs{position:absolute;left:0;top:2753px;width:1200px;height:499px;background:linear-gradient(180deg,var(--band),var(--band-dark))}
.blog-card{position:absolute;top:2891px;width:292px;height:285px;background:var(--white)}
.blog-card .pic{position:absolute;left:0;top:0;width:292px;height:163px}
.blog-card h4{position:absolute;left:15px;top:170px;width:270px;font-size:20.5px;font-weight:600;line-height:20px}
.blog-meta{position:absolute;left:16px;top:258px;width:270px;display:flex;justify-content:space-between;font-size:12.5px}

/* footer */
.site-footer{position:absolute;left:0;top:3252px;width:1200px;height:321px;background:var(--footer-bg)}
.foot-brand{position:absolute;left:107px;top:3372px;font-size:14px;font-weight:600;color:var(--muted);letter-spacing:.6px}
.foot-about{position:absolute;left:107px;top:3432px;width:228px;font-size:15px;line-height:23px}
.foot-head{position:absolute;font-size:23px;font-weight:500;text-transform:uppercase}
.foot-list{position:absolute;font-size:15.5px;line-height:23.5px}
.social{position:absolute;top:3472px;width:38px;height:38px;border:2px solid var(--ink);border-radius:50%}
.foot-rule{position:absolute;left:105px;top:3538px;width:978px;height:1.5px;background:var(--ink)}
.copyright{position:absolute;left:0;top:3544px;width:1200px;text-align:center;font-size:15px}
</style>
</head>
<body>

<header class="site-header">
  <div class="brand"><span class="brand-mark"></span>Harlow &amp; Sons</div>
  <nav class="main-nav">
    <span style="left:0">HOME</span>
    <span style="left:80px">ABOUT US</span>
    <span style="left:196px">SERVICES
      <svg width="12" height="8" viewBox="0 0 12 8"><path d="M1 1l5 5 5-5" fill="none" stroke="#111" stroke-width="1.6"/></svg></span>
    <span style="left:306px">OUR WORK</span>
    <span style="left:426px">CONTACT US</span>
  </nav>
  <div class="query-pill">FOR QUERIES<br>+1 555 010 2030</div>
</header>

<section class="hero" role="img" aria-label="Bright modern living room with grey sofa, coffee table and white kitchen behind"></section>
<div class="hero-tag">HARLOW &amp; SONS CONSTRUCTION INC</div>
<h1 class="hero-title">Welcome to<br>Harlow &amp; Sons<br>Constuction Inc</h1>
<p class="hero-copy">Lorem Ipsum is simply dummy text of the printing and typesetting industry. Lorem Ipsum has been the industry's standard dummy text ever since the 1500s</p>
<a class="btn btn-light" style="left:110px;top:470px;width:158px;height:58px">Read More</a>

<section>
  <h2 class="section-title" style="left:110px;top:762px">About Us</h2>
  <div class="about-rule"></div>
  <p class="about-copy">Lorem Ipsum is simply dummy text of the printing and typesetting industry. Lorem Ipsum has been the industry's standard dummy text ever since the 1500s Lorem Ipsum is simply dummy text of the printing and typesetting industry. Lorem Ipsum has been the industry's standard dummy text ever since the 1500s Lorem Ipsum is simply dummy text of the printing and typesetting industry. Lorem Ipsum has been the industry's standard dummy text ever since the 1500s</p>
  <a class="btn btn-dark" style="left:110px;top:1077px;width:158px;height:61px">Read More</a>
  <div class="photo" style="left:634px;top:739px;width:449px;height:427px;background:linear-gradient(135deg,#d8d4cc,#3f4a5a)" role="img" aria-label="Carpenter measuring wood in a workshop"></div>
</section>

<section class="services"></section>
<h2 class="center-title" style="top:1383px">Our Services</h2>
<div class="title-rule"></div>
<svg class="arrow" style="left:64px" width="16" height="24" viewBox="0 0 16 24"><path d="M12 3L4 12l8 9" fill="none" stroke="#fff" stroke-width="2.4"/></svg>
<svg class="arrow" style="left:1117px" width="16" height="24" viewBox="0 0 16 24"><path d="M4 3l8 9-8 9" fill="none" stroke="#fff" stroke-width="2.4"/></svg>
<article class="service-card" style="left:109px">
  <div class="pic" style="background:linear-gradient(135deg,#6b5a4a,#c9c3bb)" role="img" aria-label="Plumber fitting a kitchen sink pipe"></div>
  <h3>KITCHENS</h3>
  <p>Lorem Ipsum is simply dummy text of the printing and typesetting industry. Lorem Ipsum has been the industry's standard</p>
  <a class="btn btn-dark" style="left:156px;top:498px;width:158px;height:61px">Read More</a>
</article>
<article class="service-card" style="left:630px">
  <div class="pic" style="background:linear-gradient(180deg,#e4e6e3,#6f8a6a 55%,#3fa6a8)" role="img" aria-label="Modern house with turquoise swimming pool and garden"></div>
  <h3>POOL DESIGNS</h3>
  <p>Lorem Ipsum is simply dummy text of the printing and typesetting industry. Lorem Ipsum has been the industry's standard</p>
  <a class="btn btn-dark" style="left:147px;top:498px;width:158px;height:61px">Read More</a>
</article>

<section>
  <div class="photo" style="left:109px;top:2296px;width:432px;height:365px;background:linear-gradient(135deg,#6b6f78,#e0c14a 45%,#8b8f99)" role="img" aria-label="Smiling builder in yellow hard hat and ear defenders"></div>
  <h2 class="section-title" style="left:599px;top:2285px">Contact Us</h2>
  <div class="field" style="top:2355px">Your Name</div>
  <div class="field" style="top:2408px">Contact Number</div>
  <div class="field" style="top:2461px">Email</div>
  <div class="field" style="top:2513px;height:84px">Message</div>
  <a class="btn btn-dark" style="left:599px;top:2617px;width:158px;height:61px">Submit</a>
</section>

<section class="blogs"></section>
<h2 class="center-title" style="top:2808px">Our Blogs</h2>
<article class="blog-card" style="left:104px">
  <div class="pic" style="background:linear-gradient(135deg,#e9e6e2,#8a8580)" role="img" aria-label="Worker laying floor tiles"></div>
  <h4>Lorem Ipsum is simply dummy text of the Lorem Ipsum is simply</h4>
  <div class="blog-meta"><span>Mar. 3. 2023</span><span>.</span><span>Lorem</span><span>.</span><span>1 comment</span></div>
</article>
<article class="blog-card" style="left:447px">
  <div class="pic" style="background:linear-gradient(135deg,#9aa39a,#3e4748)" role="img" aria-label="Covered patio with outdoor kitchen and dining table"></div>
  <h4>Lorem Ipsum is simply dummy text of the Lorem Ipsum is simply</h4>
  <div class="blog-meta"><span>Mar. 3. 2023</span><span>.</span><span>Lorem</span><span>.</span><span>1 comment</span></div>
</article>
<article class="blog-card" style="left:789px">
  <div class="pic" style="background:linear-gradient(135deg,#5d7a3e,#2c3a2a 60%,#b9a043)" role="img" aria-label="Garden pond with stone edging and plants"></div>
  <h4>Lorem Ipsum is simply dummy text of the Lorem Ipsum is simply</h4>
  <div class="blog-meta"><span>Mar. 3. 2023</span><span>.</span><span>Lorem</span><span>.</span><span>1 comment</span></div>
</article>

<footer class="site-footer"></footer>
<div class="foot-brand">HARLOW &amp; SONS CONSTRUCTION INC</div>
<p class="foot-about">Lorem Ipsum is simply dummy text Lorem Ipsum is simply Lorem Ipsu simply dummy text of the Lorem</p>

<h3 class="foot-head" style="left:408px;top:3290px">Contact Info</h3>
<svg class="abs" style="left:404px;top:3335px" width="16" height="20" viewBox="0 0 16 20"><path d="M8 1a6 6 0 0 0-6 6c0 5 6 12 6 12s6-7 6-12a6 6 0 0 0-6-6z" fill="#111"/><circle cx="8" cy="7" r="2.2" fill="#fbf4f3"/></svg>
<p class="foot-list" style="left:430px;top:3335px">Lorem Ipsum is simply<br>Lorem Ipsum is simply<br>pin 888888</p>
<svg class="abs" style="left:412px;top:3411px" width="18" height="18" viewBox="0 0 24 24"><path d="M6.6 10.8a15 15 0 0 0 6.6 6.6l2.2-2.2a1 1 0 0 1 1-.25 11 11 0 0 0 3.6.6 1 1 0 0 1 1 1V20a1 1 0 0 1-1 1A17 17 0 0 1 3 4a1 1 0 0 1 1-1h3.5a1 1 0 0 1 1 1 11 11 0 0 0 .6 3.6 1 1 0 0 1-.25 1z" fill="#111"/></svg>
<p class="foot-list" style="left:437px;top:3407px">+1 555 010 2030</p>
<svg class="abs" style="left:409px;top:3442px" width="22" height="22" viewBox="0 0 24 24" fill="none" stroke="#111" stroke-width="1.4"><circle cx="12" cy="12" r="10"/><ellipse cx="12" cy="12" rx="4.5" ry="10"/><path d="M2 12h20M4 7h16M4 17h16"/></svg>
<p class="foot-list" style="left:441px;top:3441px">info@harlowsons<br>.example</p>

<h3 class="foot-head" style="left:669px;top:3290px">Navigation</h3>
<p class="foot-list" style="left:670px;top:3335px">About us<br>Services<br>Our Work<br>Contact Us</p>

<h3 class="foot-head" style="left:892px;top:3290px">Other Links</h3>
<p class="foot-list" style="left:892px;top:3335px">Privacy Policy<br>Terms and Condition<br>Careers</p>
<h3 class="foot-head" style="left:892px;top:3422px">Follow Us</h3>
<span class="social" style="left:891px" aria-label="Social link 1"></span>
<span class="social" style="left:937px" aria-label="Social link 2"></span>
<span class="social" style="left:983px" aria-label="Social link 3"></span>
<span class="social" style="left:1030px" aria-label="Social link 4"></span>

<div class="foot-rule"></div>
<p class="copyright">© 2023 HARLOW&amp;SONSCONSTRUCTION | ALLRIGHTSRESERVED</p>

</body>
</html>
```